Web Design Project

We are looking for a unified design of Corporate Website, Stationary (Including Letterhead and Envelopes), Business Cards, Email Footers and Sales & Marketing Brochures.

Color palette should include:
Black (R: 24, G:24, B:24)
Red (R:206, G:0, B:39)
Dark Grey (R:51, G:51, B:51)
Light Grey/Silver (R:203, G:203, B:203)

As we do business in North America and the UK, designs should be reflective of standard sizing for both regions.

Check out our website to better understand who we are: www.KVRT.com and a copy of our Logo has been uploaded for reference.
Updates

Hello all, we had not anticipated the volume of unique, high quality designs we have received, thank you all for your submissions. A team review of all designs will take place the week of December 8th, and final decisions and selections made. Thank you again

Target Market(s)

Automotive Parts Wholesalers, Vehicle Repair Specialists, Automotive Parts Manufacturers, Automotive Insurance

Industry/Entity Type

Business

Font styles to use
Sans Serif

Requirements
Must have
• - Color palette should include:
- Black (R: 24, G:24, B:24)
- Red (R:206, G:0, B:39)
- Dark Grey (R:51, G:51, B:51)
- Light Grey/Silver (R:203, G:203, B:203)
Should not have
• No Animations

```html
<!DOCTYPE html>
<html lang="en">
<head>
<meta charset="utf-8">
<title>Vantix Parts Solutions</title>
<link href="https://fonts.googleapis.com/css2?family=Nunito+Sans:wght@300;400;600;700;800&display=swap" rel="stylesheet">
<style>
:root{
  --black:#181818;
  --red:#ce0027;
  --dark:#333333;
  --silver:#cbcbcb;
  --panel:#efefef;
  --text:#222;
  --white:#fff;
}
*{box-sizing:border-box;margin:0;padding:0}
html,body{width:872px;height:1200px;overflow:hidden;background:var(--white)}
body{font-family:"Nunito Sans",sans-serif;color:var(--text);position:relative}
.abs{position:absolute}
.rule{position:absolute;left:0;width:872px;height:4px;
  background:repeating-linear-gradient(135deg,#9a9a9a 0 1px,transparent 1px 3px)}
/* header */
.brand{left:85px;top:18px;display:flex;align-items:center;gap:8px}
.brand-mark{width:38px;height:38px;border-radius:50%;border:3px solid #8a8a8a}
.brand-name{font-size:18px;font-weight:800;color:var(--black);letter-spacing:.5px;line-height:1}
.brand-name small{display:block;font-size:10px;font-weight:600;color:#8a8a8a;letter-spacing:2.6px;margin-top:2px}
.langs{left:468px;top:23px;display:flex;gap:5px}
.langs span{width:16px;height:11px;background:var(--silver);display:block}
.btn{position:absolute;display:flex;align-items:center;justify-content:center;color:var(--white);font-size:12.5px}
.btn-dark{background:var(--black)}
.btn-red{background:var(--red)}
.nav{left:0;top:72px;width:872px;height:46px;background:linear-gradient(#2e2e2e,var(--black));
  display:flex;justify-content:center;align-items:center;gap:21.5px}
.nav a{color:#e6e6e6;font-size:10.6px;text-decoration:none;text-transform:uppercase}
/* hero */
.hero{left:0;top:120px;width:872px;height:355px;background:var(--red)}
.hero-car{left:40px;top:66px;width:420px;height:214px;border-radius:40% 50% 20% 20%;
  background:radial-gradient(ellipse at 50% 45%,#e83447,#9d0019 70%,var(--red) 100%)}
.hero h1{right:109px;top:102px;font-size:24px;font-weight:400;color:var(--white);text-align:right}
.hero .sub{right:110px;top:137px;font-size:12.5px;color:var(--white)}
.video{left:501px;top:211px;width:261px;height:34px;border:1px solid #f09aa8;
  display:flex;align-items:center;gap:8px;padding-left:8px;color:var(--white);font-size:10px;font-weight:700}
.arrows{left:710px;top:278px}
/* makes */
.makes{left:60px;top:488px;width:762px;display:flex;justify-content:space-between;align-items:center}
.makes span{width:24px;height:24px;border-radius:50%;background:#bdbdbd;display:block}
.makes span.sq{border-radius:3px;width:30px;height:16px;background:#444}
/* opportunity */
.heading{left:0;width:872px;text-align:center;font-weight:400;color:var(--text)}
.copy{left:0;width:872px;text-align:center;font-size:12px;line-height:14px}
.card{position:absolute;top:727px;width:294px;height:150px;background:var(--panel);border:1px solid #e0e0e0;padding:14px 10px 0 11px}
.card h3{font-size:13.5px;font-weight:400;margin-bottom:13px}
.card p{font-size:9.2px;line-height:11.4px;text-align:justify;margin-bottom:11px}
.award{right:14px;bottom:14px;display:flex;align-items:center;gap:6px;color:var(--red);font-weight:800;font-size:12px}
.award i{width:30px;height:30px;border-radius:50%;background:var(--red);display:block}
/* testimonial */
.portrait{left:174px;top:929px;width:112px;height:112px;border-radius:50%;background:radial-gradient(circle at 40% 40%,#d9d9d9,#6d6d6d)}
.quote{left:299px;top:953px;width:425px;font-size:12px;line-height:14.5px}
.cite{left:299px;top:993px;font-size:10px;color:var(--red)}
/* footer */
.footer{left:0;top:1064px;width:872px;height:136px;background:var(--dark);color:#e6e6e6}
.footer h4{position:absolute;font-size:12px;font-weight:400;color:#e0e0e0}
.footer ul{position:absolute;list-style:none;font-size:10px;line-height:17.5px;color:#ddd}
.map{left:457px;top:40px;width:141px;height:71px;background:linear-gradient(135deg,#e7e2c8,#d6dcc4 60%,#bfd3e0)}
.social{left:650px;top:49px;display:flex;gap:9px}
.social span{width:20px;height:20px;border-radius:50%;display:block}
.copyright{left:634px;top:103px;font-size:10px;color:#ddd}
</style>
</head>
<body>
<header>
  <div class="abs brand"><span class="brand-mark"></span><div class="brand-name">VANTIX<small>parts solutions</small></div></div>
  <div class="abs langs"><span></span><span></span><span></span></div>
  <div class="btn btn-dark" style="left:546px;top:14px;width:94px;height:33px">Supplier Login</div>
  <div class="btn btn-red" style="left:646px;top:14px;width:116px;height:33px">Vantix Awards</div>
</header>
<div class="rule" style="top:67px"></div>
<nav class="abs nav">
  <a>Home</a><a>Intelligent Sales &amp; Marketing</a><a>Vantix Awards</a><a>References</a><a>About Us</a><a>Careers</a><a>Contact Us</a>
</nav>
<div class="rule" style="top:117px;background:repeating-linear-gradient(135deg,#e07080 0 1px,transparent 1px 3px)"></div>
<section class="abs hero">
  <div class="abs hero-car" role="img" aria-label="Red sports coupe photograph"></div>
  <h1 class="abs">Genuine Parts Sales &amp; Marketing</h1>
  <div class="abs sub">We offer a unique multi-brand solution</div>
  <div class="btn btn-dark" style="left:665px;top:170px;width:93px;height:32px;font-size:13px">Learn More</div>
  <div class="abs video">
    <svg width="20" height="20" viewBox="0 0 20 20"><circle cx="10" cy="10" r="9" fill="none" stroke="#fff" stroke-width="1.3"/><path d="M8 6l5 4-5 4z" fill="#fff"/></svg>
    CLICK HERE TO WATCH OUR CORPORATE VIDEO
  </div>
  <svg class="abs arrows" width="40" height="28" viewBox="0 0 40 28"><path d="M14 2L3 14l11 12M26 2l11 12-11 12" fill="none" stroke="#fff" stroke-width="1.4"/></svg>
</section>
<div class="rule" style="top:476px"></div>
<div class="abs makes" role="img" aria-label="Row of vehicle make badges">
  <span class="sq" style="width:42px"></span><span></span><span></span><span></span><span class="sq"></span><span></span><span></span><span></span><span class="sq"></span><span class="sq"></span><span></span><span class="sq"></span><span></span><span class="sq"></span><span class="sq"></span><span class="sq"></span><span class="sq"></span><span class="sq"></span><span class="sq" style="width:24px;height:24px"></span><span></span>
</div>
<div class="rule" style="top:522px"></div>
<h2 class="abs heading" style="top:532px;font-size:25px">The Opportunity</h2>
<div class="rule" style="top:568px"></div>
<p class="abs copy" style="top:583px">OE WHOLESALE Parts provide significant opportunities for both OE dealership suppliers and<br>repairers to capture new and incremental profits.</p>
<p class="abs copy" style="top:624px">On behalf of our local ‘Best in Class’ parts WHOLESALERS our team of qualified parts experts<br>work with repairers to maximize these profits.</p>
<div class="btn btn-red" style="left:389px;top:669px;width:94px;height:32px;font-size:13px">Learn More</div>
<div class="rule" style="top:712px"></div>
<div class="card" style="left:131px">
  <h3>The Vantix Multi-Brand Solution</h3>
  <p>We offer a unique multi-brand solution to both OE suppliers and the automotive repairers by combining professionally managed parts programs that are shared between non-competing suppliers.</p>
  <p>This shared approach provides increased value and convenience to the repairer as they only deal with one parts professional for all their genuine parts needs.</p>
</div>
<div class="card" style="left:445px">
  <h3>Vantix Parts Rewards</h3>
  <p>Our Vantix Awards WHOLESALE parts loyalty program is designed specifically for the automotive repair industry. Repairers earn Reward Points from multiple suppliers, not just one earning bigger, better Rewards faster than any other program in our industry.</p>
  <div class="abs award"><i></i>VANTIX AWARDS</div>
</div>
<div class="rule" style="top:884px"></div>
<h2 class="abs heading" style="top:891px;font-size:18px;padding-right:50px">Testimonials</h2>
<div class="rule" style="top:921px"></div>
<svg class="abs" style="left:138px;top:959px" width="20" height="34" viewBox="0 0 20 34"><path d="M17 2L3 17l14 15" fill="none" stroke="#333" stroke-width="1.2"/></svg>
<div class="abs portrait" role="img" aria-label="Portrait photograph of a customer"></div>
<p class="abs quote">This has been a great program to promote loyalty from shops and a great tool to help increase our wholesale parts revenue.</p>
<div class="abs cite">Dan Morrow, Parts Manager Harbor Motors</div>
<svg class="abs" style="left:727px;top:959px" width="20" height="34" viewBox="0 0 20 34"><path d="M3 2l14 15L3 32" fill="none" stroke="#333" stroke-width="1.2"/></svg>
<div class="rule" style="top:1060px"></div>
<footer class="abs footer">
  <h4 style="left:108px;top:14px">Quick Links</h4>
  <ul style="left:111px;top:44px"><li>Home</li><li>Inteligent Sales &amp; Marketing</li><li>Vantix Awards</li><li>References</li></ul>
  <ul style="left:252px;top:42px"><li>About Us</li><li>Careers</li><li>Contact Us</li></ul>
  <h4 style="left:334px;top:14px">Contact Us</h4>
  <ul style="left:336px;top:42px"><li>X12 . Lorium ipsum</li><li>Phone: +13 6 555 0142</li><li>112 Mill Lane</li><li>New Zealand</li></ul>
  <div class="abs map" role="img" aria-label="Street map of office location"></div>
  <h4 style="left:651px;top:14px">Follow Us</h4>
  <div class="abs social"><span style="background:#3b5998"></span><span style="background:#1da1f2"></span><span style="background:#0e76a8"></span><span style="background:#d9252a"></span></div>
  <div class="abs copyright">© 2014 Vantix Parts Solutions</div>
</footer>
</body>
</html>
```